New Print Material Needed for Renovation Company

We are looking to update our current Print Material to reflect the current process we offer to our clients. A lot of the information is also outdated along with many of the photos that are currently being used. We are a renovation company that specializes in residential and commercial renovations and custom builds.This project is MULTIPLE pages. We will pay the chosen designer an extra fee for the designing 3-4 additional pages that are similar to the chosen design. Attached is our current Print Material. We are hoping to update the look of them and some of the messaging. Our current company colors are white, blue and light grey and it will remain that way.

Industry/Entity Type

Construction Company

Font styles to use
Sans Serif

Colors
3176b5
ffffff

Requirements
Must have
• Easy to explain the process
• Easy to read and understand let alone
• Easy to navigate
Nice to have
• As much creativity as possible
Should not have
• no confusing text
• no confusing layout

```html
<!DOCTYPE html>
<html lang="en">
<head>
<meta charset="utf-8">
<title>Master Builder Timeline</title>
<link rel="stylesheet" href="https://fonts.googleapis.com/css2?family=Arimo:wght@400;700&family=Source+Sans+3:wght@400;600&display=swap">
<style>
  :root {
    --navy: #0d5186;
    --step-blue: #1177be;
    --rail-blue: #2c75b8;
    --sky: #29abe2;
    --panel-grey: #e6e7e9;
    --arrow-taupe: #9c8b7d;
    --ink: #111111;
    --white: #ffffff;
  }
  * { margin: 0; padding: 0; box-sizing: border-box; }
  html, body { width: 1200px; height: 776px; overflow: hidden; background: var(--white); }
  .sheet { position: relative; width: 1200px; height: 776px; font-family: "Source Sans 3", sans-serif; color: var(--ink); }

  .program-badge { position: absolute; left: 50px; top: 62px; display: flex; align-items: center; gap: 10px;
    font-family: "Arimo", sans-serif; font-size: 18px; font-weight: 700; color: var(--navy); line-height: 1.15; }
  .program-badge .dot { flex: none; width: 48px; height: 48px; border-radius: 50%; background: var(--sky); }

  .title { position: absolute; left: 245px; top: 52px; font-family: "Arimo", sans-serif; font-size: 66px; letter-spacing: -1px; white-space: nowrap; line-height: 1; }
  .title .light { color: var(--sky); font-weight: 400; }
  .title .bold { color: var(--ink); font-weight: 700; }
  .title .outline { color: var(--white); -webkit-text-stroke: 2px var(--ink); font-weight: 400; }

  .partner { position: absolute; left: 1025px; top: 19px; width: 148px; height: 108px; background: var(--navy);
    display: flex; align-items: center; gap: 8px; padding: 0 10px; color: var(--white); font-family: "Arimo", sans-serif; font-size: 13px; line-height: 1.2; }
  .partner .dot { flex: none; width: 30px; height: 30px; border-radius: 50%; border: 3px solid var(--white); }

  .phase { position: absolute; top: 185px; height: 72px; background: var(--navy); border-radius: 12px;
    display: flex; align-items: center; color: var(--white); font-family: "Arimo", sans-serif; font-size: 38px; }
  .phase .num { width: 36px; height: 36px; border: 2px solid var(--white); border-radius: 50%; font-size: 22px;
    display: flex; align-items: center; justify-content: center; margin: 0 14px 0 7px; }
  .phase-design { left: 27px; width: 181px; }
  .phase-plan { left: 448px; width: 185px; }
  .phase-plan .num, .phase-build .num { margin-right: 30px; margin-left: 11px; }
  .phase-build { left: 840px; top: 188px; height: 65px; width: 186px; }
  .flow-arrow { position: absolute; top: 202px; }

  .panel { position: absolute; left: 30px; top: 270px; width: 1158px; height: 498px; background: var(--panel-grey); }
  .rail { position: absolute; top: 285px; width: 6px; height: 463px; background: var(--rail-blue); }

  .step-num { position: absolute; width: 34px; height: 34px; border-radius: 50%; background: var(--navy);
    box-shadow: 0 0 0 1px var(--rail-blue); color: var(--white); font-family: "Arimo", sans-serif; font-size: 23px;
    display: flex; align-items: center; justify-content: center; }
  .step-title { position: absolute; height: 41px; background: var(--step-blue); border-radius: 14px;
    color: var(--white); font-family: "Arimo", sans-serif; font-size: 23px; padding-left: 10px; display: flex; align-items: center; }
  .step-title::before { content: ""; position: absolute; left: -14px; top: 12px; border-style: solid;
    border-width: 8px 15px 8px 0; border-color: transparent var(--step-blue) transparent transparent; }
  .step-text { position: absolute; width: 292px; font-size: 18.5px; line-height: 21px; text-align: justify; }
  .duration { position: absolute; font-family: "Arimo", sans-serif; font-size: 17px; display: flex; align-items: center; gap: 10px; white-space: nowrap; }
  .duration .field { width: 193px; height: 30px; border: 1.5px solid var(--ink); border-radius: 15px; background: var(--panel-grey); }
</style>
</head>
<body>
<div class="sheet">
  <div class="program-badge"><span class="dot"></span><span>Master<br>Builder</span></div>
  <h1 class="title"><span class="light">Master</span> <span class="bold">Builder</span> <span class="outline">Timeline</span></h1>
  <div class="partner"><span class="dot"></span><span>Northgate General Contractors</span></div>

  <div class="phase phase-design"><span class="num">1</span>Design</div>
  <svg class="flow-arrow" style="left:242px" width="135" height="38" viewBox="0 0 135 38">
    <line x1="0" y1="19" x2="100" y2="19" stroke="var(--arrow-taupe)" stroke-width="4" stroke-dasharray="11 9"/>
    <path d="M99 0 L133 19 L99 38 L108 19 Z" fill="var(--arrow-taupe)"/>
  </svg>
  <div class="phase phase-plan"><span class="num">2</span>Plan</div>
  <svg class="flow-arrow" style="left:666px" width="135" height="38" viewBox="0 0 135 38">
    <line x1="0" y1="19" x2="100" y2="19" stroke="var(--arrow-taupe)" stroke-width="4" stroke-dasharray="11 9"/>
    <path d="M99 0 L133 19 L99 38 L108 19 Z" fill="var(--arrow-taupe)"/>
  </svg>
  <div class="phase phase-build"><span class="num">3</span>Build</div>

  <div class="panel"></div>
  <div class="rail" style="left:28px"></div>
  <div class="rail" style="left:444px"></div>
  <div class="rail" style="left:836px"></div>

  <!-- Design column -->
  <div class="step-num" style="left:14px;top:274px">1</div>
  <div class="step-title" style="left:66px;top:271px;width:342px">INITIAL DESIGN MEETING</div>
  <p class="step-text" style="left:75px;top:318px">The first step of the design process is to confirm the design concept you have envisioned.</p>
  <div class="duration" style="left:75px;top:389px">1 - 2 weeks <span class="field"></span></div>

  <div class="step-num" style="left:14px;top:435px">2</div>
  <div class="step-title" style="left:66px;top:432px;width:342px">SECOND DESIGN MEETING</div>
  <p class="step-text" style="left:76px;top:485px">Our designers work directly with you to ensure the measurements line up with your design ideas.</p>
  <div class="duration" style="left:75px;top:556px">1 - 2 weeks <span class="field"></span></div>

  <div class="step-num" style="left:14px;top:606px">3</div>
  <div class="step-title" style="left:66px;top:603px;width:338px">FINAL DESIGN MEETING</div>
  <p class="step-text" style="left:74px;top:654px">Any last minute or final revisions will be completed within three days of this meeting.</p>
  <div class="duration" style="left:74px;top:716px">1 - 3 weeks <span class="field"></span></div>

  <!-- Plan column -->
  <div class="step-num" style="left:430px;top:274px">4</div>
  <div class="step-title" style="left:480px;top:271px;width:308px">MATERIAL SELECTION</div>
  <p class="step-text" style="left:494px;top:322px">Our material collection coordinator will work with you to ensure all the right materials.</p>
  <div class="duration" style="left:492px;top:389px">1 - 4 weeks <span class="field"></span></div>

  <div class="step-num" style="left:430px;top:435px">5</div>
  <div class="step-title" style="left:480px;top:432px;width:310px">ENGINEER DRAWINGS</div>
  <p class="step-text" style="left:495px;top:485px">The final permit drawings will be sent to engineers to ensure structural integrity.</p>
  <div class="duration" style="left:494px;top:556px">2 - 4 weeks <span class="field"></span></div>

  <div class="step-num" style="left:430px;top:606px">6</div>
  <div class="step-title" style="left:480px;top:603px;width:310px">BUILDING PERMIT PLANS</div>
  <p class="step-text" style="left:495px;top:651px">Permit drawings will begin once the build has been signed and initial payments have been made.</p>
  <div class="duration" style="left:494px;top:717px">3 - 25 weeks <span class="field" style="width:184px"></span></div>

  <!-- Build column -->
  <div class="step-num" style="left:822px;top:274px">7</div>
  <div class="step-title" style="left:873px;top:271px;width:309px">MATERIAL FINALISATION</div>
  <p class="step-text" style="left:883px;top:322px;width:283px">A lead designer will finalize any revisions you may have of your material selection.</p>
  <div class="duration" style="left:884px;top:389px">2 - 4 weeks <span class="field" style="width:177px"></span></div>

  <div class="step-num" style="left:822px;top:435px">8</div>
  <div class="step-title" style="left:873px;top:432px;width:309px">CONSTRUCTION PLANS</div>
  <p class="step-text" style="left:888px;top:485px;width:280px">The drawings will be updated within 24 hours once the permits have been approved &amp; received.</p>
  <div class="duration" style="left:887px;top:556px">2 - 6 weeks <span class="field" style="width:175px"></span></div>

  <div class="step-num" style="left:822px;top:606px">9</div>
  <div class="step-title" style="left:873px;top:603px;width:309px">SCHEDULING</div>
  <p class="step-text" style="left:892px;top:651px;width:272px">All designs, dates, permits have been completed. The project is ready to get underway.</p>
  <div class="duration" style="left:887px;top:717px">2 - 4 weeks <span class="field" style="width:175px"></span></div>
</div>
</body>
</html>
```